indoor tennis and sports center( club)

we need a logo for a new business venture, it will be for business cards and for presentations.
presentations for potential investors and authorities.
the design needs to communicate the sport and a community of tennis players
the center includes a tennis academy, and sports club with training sessions for all ages

Reason: so that I can get some more feedback on my side as to te design we want

Target Market(s)

potential investors or partners

Industry/Entity Type

Business

Contact Information for Business Card

i need the name of the club
names of the partners
slogan" changing lives through tennis" on the front
the clubs three main goals are ports education , academy and a community club

Colors
3176b5
33b8a4
fbee3d
0dac94
acd036

Requirements
Must have
• a strong logo
• names of the partners
• web site and email address
• tel number
Nice to have
• a connection between the different aspects of the club

```html
<!DOCTYPE html>
<html lang="en">
<head>
<meta charset="utf-8">
<title>Baseline Hall – Business Cards</title>
<link rel="stylesheet" href="https://fonts.googleapis.com/css2?family=Open+Sans:wght@300;400;600;700&display=swap">
<style>
  :root {
    --backdrop: #ece9e4;
    --kraft-light: #c9ad84;
    --kraft: #b99a6f;
    --kraft-dark: #a88a60;
    --ink: #1c1712;
    --card-shadow: rgba(60, 45, 25, 0.25);
  }
  * { margin: 0; padding: 0; box-sizing: border-box; }
  html, body {
    width: 1200px;
    height: 900px;
    overflow: hidden;
    background: var(--backdrop);
    font-family: "Open Sans", Arial, sans-serif;
    color: var(--ink);
  }
  .canvas { position: relative; width: 1200px; height: 900px; }

  .card {
    position: absolute;
    background: linear-gradient(135deg, var(--kraft-light) 0%, var(--kraft) 55%, var(--kraft-dark) 100%);
    box-shadow: 0 6px 18px var(--card-shadow);
    text-align: center;
  }

  /* Contact side */
  .card--contact { left: 238px; top: 62px; width: 555px; height: 342px; }
  .person-name {
    position: absolute; left: 0; right: 0; top: 56px;
    font-weight: 700; font-size: 18px; letter-spacing: 0.3px;
  }
  .person-role {
    position: absolute; left: 0; right: 0; top: 81px;
    font-size: 14.5px;
  }
  .rule {
    position: absolute; height: 1px; background: var(--ink);
  }
  .rule--top { left: 210px; width: 134px; top: 121px; }
  .rule--bottom { left: 205px; width: 146px; top: 234px; }
  .contact-list {
    position: absolute; left: 0; right: 0; top: 148px;
    list-style: none; font-size: 14.5px; line-height: 20.5px;
  }
  .slogan {
    position: absolute; left: 0; right: 0; top: 263px;
    font-size: 16px; letter-spacing: 1.1px;
  }

  /* Brand side */
  .card--brand { left: 458px; top: 518px; width: 559px; height: 342px; }
  .brand-name {
    position: absolute; left: 80px; top: 118px;
    font-weight: 300; font-size: 50px; letter-spacing: 0.5px; line-height: 1;
    display: flex; align-items: center; gap: 14px;
  }
  .brand-dot {
    width: 18px; height: 18px; border-radius: 50%; background: var(--ink);
  }
  .brand-subtitle {
    position: absolute; left: 82px; top: 181px;
    font-weight: 600; font-size: 15px;
  }
  .services {
    position: absolute; left: 0; right: 0; top: 234px;
    font-size: 20px; word-spacing: 2px;
  }
  .services .divider { margin: 0 10px; }
  .tagline {
    position: absolute; left: 0; right: 0; top: 278px;
    font-size: 17px; letter-spacing: 3.4px;
  }
</style>
</head>
<body>
<main class="canvas">

  <section class="card card--contact" aria-label="Business card, contact side">
    <h1 class="person-name">DANIEL AVNER</h1>
    <p class="person-role">Managing Director</p>
    <div class="rule rule--top"></div>
    <ul class="contact-list">
      <li>044-987 654 321</li>
      <li>hello@baselinehall.com</li>
      <li>www.baselinehall.com</li>
    </ul>
    <div class="rule rule--bottom"></div>
    <p class="slogan">CHANGING LIVES THROUGH TENNIS</p>
  </section>

  <section class="card card--brand" aria-label="Business card, brand side">
    <h2 class="brand-name">Baseline Hall <span class="brand-dot"></span></h2>
    <p class="brand-subtitle">Coastal Indoor Racquets and Sports Club</p>
    <p class="services">Indoor club<span class="divider">|</span>Academy<span class="divider">|</span>Education</p>
    <p class="tagline">BUILDING A COMMUNITY</p>
  </section>

</main>
</body>
</html>
```